Website for a company offering full serivce charging solutions for electric cars

The company "mero-kant" (english: "mero-edge") offering all-in-one-solutions for charging infrastructure for electric mobility.

There are four products:
1- Wallboxes for single-family homes
2- Solutions for property devloper/-management for property parking space
3- All-in-one-charging solution for municipalities/communities
4- Solutions for tourism/hotels/holiday appartments

The Website structure:
1. Main Page
2.1. Product Page Single Homes
2.2. Product Page Property Management / Parking
2.3. Product Page Municipality
2.4. Product Page Tourism
3. Contact Form / Request for information
4. Imprint / Legal

The Website should be built on Wordpress with a powerful possibility to simply add/modify specific landing pages.

We would like you to implement the website later and also maintain it if possible, but we would be able to do minor modifications by ourselfs (for A/B-Testing)

The website should be clear and simple, easy to understand.
Target group is mainly B2C without deeper knowledge of that topic.

It should suggest, that we will provide a very simple way to get the charging infrastructure done.

We need a contact form, maybe we will use Hubspot later.

Attached you will find a draft of the main page and a landing page (for 2.2) - it is just the content, please ignore the design. We would love to let you create a suitable design.
Also you will find some drafts a bit different for the same story.

I added also a few stock photos, but they don't need to be used! If you have better ideas, you are welcome!

Industry/Entity Type

Charging/Electric mobility

Number of Pages Required

2 page

Font styles to use
Sans Serif

Requirements
Must have
• Based on Wordpress, and the designer should be able to implement it on Wordpress on a later step

```html
<!DOCTYPE html>
<html lang="de">
<head>
<meta charset="utf-8">
<title>mero-kant.de – Charging Station for All Businesses</title>
<link href="https://fonts.googleapis.com/css2?family=Jost:wght@400;500;600&family=Poppins:wght@600;700&display=swap" rel="stylesheet">
<style>
:root{
  --pink:#ec0c9f;
  --purple:#7a5bc8;
  --ink:#1c1c1c;
  --text:#555;
  --muted:#8a8a8a;
  --soft:#f7f7f7;
  --line:#e6e6e6;
  --footer:#202020;
  --star:#f5b301;
}
*{box-sizing:border-box;margin:0;padding:0}
html,body{width:1200px;height:4773px;overflow:hidden}
body{font-family:"Jost",sans-serif;color:var(--ink);background:#fff;position:relative}
section,header,footer{position:absolute;left:0;width:1200px}

/* header */
.site-header{top:0;height:93px;background:#fff}
.brand{position:absolute;left:60px;top:28px;display:flex;align-items:center;gap:10px;font-family:"Jost",sans-serif;font-weight:600;font-size:25px;color:var(--ink)}
.brand-mark{width:14px;height:14px;border-radius:50%;background:var(--pink)}
.main-nav{position:absolute;top:36px;left:0;width:1200px;font-size:15px;font-weight:500}
.main-nav a{position:absolute;color:var(--ink);text-decoration:none}
.main-nav a.active{border-bottom:2px solid var(--ink);padding-bottom:3px}
.nav-dot{position:absolute;left:1011px;top:16px;width:5px;height:5px;border-radius:50%;background:var(--ink)}
.search{position:absolute;left:1116px;top:34px}

/* hero */
.hero{top:93px;height:697px;overflow:hidden}
.hero-photo{position:absolute;inset:0;background:linear-gradient(100deg,#f3f5fb 0%,#e9edf7 35%,#9fb2e6 55%,#3d5be0 72%,#1d34b8 85%,#7fa0ff 100%)}
.hero-copy{position:absolute;left:72px;top:170px}
.hero-kicker{font-size:17px;font-weight:500;margin-bottom:18px}
.hero-title{font-family:"Poppins",sans-serif;font-weight:700;font-size:70px;line-height:81px;letter-spacing:.5px}
.hero-title .pink{color:var(--pink)}
.btn{display:inline-flex;align-items:center;justify-content:center;color:#fff;text-decoration:none;font-size:13px;font-weight:500}
.btn-purple{background:var(--purple);width:219px;height:45px;margin-top:24px}

/* features */
.features{top:790px;height:664px;text-align:center}
.eyebrow{font-size:11px;font-weight:600;letter-spacing:1.8px;text-transform:uppercase}
.features .eyebrow{margin-top:101px}
.section-title{font-family:"Jost",sans-serif;font-weight:400;font-size:47px;line-height:50px;margin-top:18px}
.feature-row{position:absolute;top:300px;left:0;width:1200px}
.feature{position:absolute;width:260px;margin-left:-130px;text-align:center}
.feature svg{display:block;margin:0 auto}
.feature h3{font-weight:500;font-size:21px;margin-top:22px}
.feature p{font-size:13px;color:var(--muted);margin-top:6px}
.feature .more{display:flex;gap:4px;justify-content:center;margin-top:18px}
.feature .more i{width:4px;height:4px;border-radius:50%;background:#ccc}
.link-underline{position:absolute;left:0;width:1200px;top:535px;font-size:14px;font-weight:500}
.link-underline span{border-bottom:2px solid var(--ink);padding-bottom:6px}

/* plans */
.plans{top:1454px;height:1004px;background:var(--soft)}
.plan{position:absolute;top:94px;width:343px;background:#fff;border:3px solid var(--purple)}
.plan.pink{border-color:var(--pink)}
.plan-head{height:101px;background:var(--purple);color:#fff;text-align:center;padding-top:16px}
.plan.pink .plan-head{background:var(--pink)}
.plan-head h3{font-weight:500;font-size:19px;margin-top:8px}
.plan ul{list-style:none;padding:22px 22px 22px 26px}
.plan li{display:flex;gap:10px;font-size:14.5px;line-height:24px;color:#333;margin-bottom:9px}
.plan li svg{flex:0 0 22px;margin-top:2px}

/* photo band */
.photo-band{top:2458px;height:802px;background:radial-gradient(circle at 68% 55%,#3b63ff 0%,#2244d8 18%,#c9cfe0 40%,#eceef3 60%,#b9bcc4 85%,#6e7078 100%)}

/* sustainability */
.sustain{top:3260px;height:722px;background:var(--soft)}
.sustain-photo{position:absolute;left:63px;top:94px;width:434px;height:535px;background:linear-gradient(160deg,#4b4f72 0%,#8a8fb5 40%,#3c4a9a 65%,#c9d16a 85%,#2a2d3a 100%)}
.sustain-copy{position:absolute;left:619px;top:170px;width:470px}
.sustain-copy .section-title{font-size:46px;line-height:50px;margin-top:14px}
.sustain-copy p{font-size:14.5px;line-height:24px;color:var(--text);margin-top:18px}
.ticks{list-style:none;margin-top:26px}
.ticks li{display:flex;gap:12px;align-items:center;font-size:14.5px;margin-bottom:9px}
.btn-pink{background:var(--pink);width:142px;height:45px;margin-top:36px}

/* testimonials */
.reviews{top:3982px;height:638px;background:var(--soft);overflow:hidden}
.review{position:absolute;top:10px;width:256px;background:#fff;padding:64px 34px 0 34px}
.stars{color:var(--star);font-size:15px;letter-spacing:1px}
.review p{font-size:14.5px;line-height:24px;color:#444;margin-top:26px}
.review h4{font-size:15.5px;font-weight:600;margin-top:48px}
.review small{display:block;font-size:12px;color:var(--muted);margin-top:6px}
.slider-dots{position:absolute;top:562px;left:0;width:1200px;display:flex;justify-content:center;gap:9px}
.slider-dots i{width:6px;height:6px;border-radius:50%;background:#ddd}
.slider-dots i.on{background:var(--pink)}

/* footer */
.site-footer{top:4620px;height:153px;background:var(--footer);color:#fff;font-size:13.5px;line-height:23px}
.footer-address{position:absolute;left:63px;top:48px}
.footer-contact{position:absolute;left:430px;top:48px}
.socials{position:absolute;left:798px;top:57px;display:flex;gap:8px}
.socials span{width:34px;height:34px;border-radius:50%;border:1px solid #555;display:block}
.to-top{position:absolute;left:1136px;top:88px}
</style>
</head>
<body>

<header class="site-header">
  <div class="brand"><span class="brand-mark"></span>mero-kant.de</div>
  <nav class="main-nav">
    <a class="active" style="left:645px">Lösungen</a>
    <a style="left:737px">Unternehmen</a>
    <a style="left:856px">Services</a>
    <a style="left:940px">Karriere</a>
    <a style="left:1022px">Kontakt</a>
  </nav>
  <span class="nav-dot"></span>
  <svg class="search" width="22" height="22" viewBox="0 0 22 22" fill="none" stroke="#1c1c1c" stroke-width="2"><circle cx="9" cy="9" r="7"/><path d="M14 14l6 6"/></svg>
</header>

<section class="hero">
  <div class="hero-photo" role="img" aria-label="Photo of an electric car being charged, plug glowing with blue light"></div>
  <div class="hero-copy">
    <p class="hero-kicker">Powering Our Sustainable Future</p>
    <h1 class="hero-title"><span class="pink">Charging</span><br><span class="pink">Station</span> for All<br>Businesses</h1>
    <a class="btn btn-purple">Explore Our Products</a>
  </div>
</section>

<section class="features">
  <p class="eyebrow">New Generation</p>
  <h2 class="section-title">Perfomance! Hello<br>Open Roads</h2>
  <div class="feature-row">
    <div class="feature" style="left:187px">
      <svg width="44" height="54" viewBox="0 0 44 54" fill="none" stroke="#ec0c9f" stroke-width="2"><path d="M22 4a16 16 0 0 1 16 16c0 12-16 26-16 26S6 32 6 20A16 16 0 0 1 22 4z"/><path d="M24 11l-7 11h6l-3 9 8-12h-6z"/></svg>
      <h3>Public Drivers</h3><p>Sed do eiusm od tempor</p><div class="more"><i></i><i></i><i></i></div>
    </div>
    <div class="feature" style="left:463px">
      <svg width="54" height="54" viewBox="0 0 54 54" fill="none" stroke="#ec0c9f" stroke-width="2"><rect x="8" y="6" width="22" height="42" rx="2"/><rect x="12" y="11" width="14" height="10"/><path d="M30 20h6v20a4 4 0 0 0 8 0V16"/><path d="M41 10v6h6v-6"/><path d="M4 48h30"/></svg>
      <h3>Work Charging</h3><p>Sed do eiusm od tempor</p><div class="more"><i></i><i></i><i></i></div>
    </div>
    <div class="feature" style="left:737px">
      <svg width="40" height="54" viewBox="0 0 40 54" fill="none" stroke="#ec0c9f" stroke-width="2"><circle cx="20" cy="18" r="14"/><path d="M22 9l-6 10h5l-2 8 7-11h-5z"/><path d="M14 32v8h12v-8M17 40v8M23 40v8"/></svg>
      <h3>Fleet Charging</h3><p>Sed do eiusm od tempor</p><div class="more"><i></i><i></i><i></i></div>
    </div>
    <div class="feature" style="left:1013px">
      <svg width="52" height="54" viewBox="0 0 52 54" fill="none" stroke="#ec0c9f" stroke-width="2"><rect x="6" y="6" width="18" height="18" rx="3"/><path d="M11 2v4M19 2v4M15 24v10a8 8 0 0 0 16 0V22a6 6 0 0 1 12 0v10"/><rect x="38" y="32" width="10" height="14" rx="2"/></svg>
      <h3>Public Charging</h3><p>Sed do eiusm od tempor</p><div class="more"><i></i><i></i><i></i></div>
    </div>
  </div>
  <p class="link-underline"><span>Get In Touch</span></p>
</section>

<section class="plans">
  <article class="plan" style="left:63px">
    <div class="plan-head">
      <svg width="38" height="34" viewBox="0 0 38 34" fill="none" stroke="#fff" stroke-width="2"><circle cx="19" cy="10" r="6"/><circle cx="8" cy="13" r="4"/><circle cx="30" cy="13" r="4"/><path d="M9 32v-6a10 10 0 0 1 20 0v6M2 30v-4a6 6 0 0 1 6-6M36 30v-4a6 6 0 0 0-6-6"/></svg>
      <h3>als Privatkunde</h3>
    </div>
    <ul>
      <li><svg width="22" height="22" viewBox="0 0 22 22"><circle cx="11" cy="11" r="11" fill="#7a5bc8"/><path d="M6 11l3.5 3.5L16 8" stroke="#fff" stroke-width="2.2" fill="none"/></svg>Bestandsanalyse mit umfangreicher Beratung über die Möglichkeiten der Umsetzung</li>
      <li><svg width="22" height="22" viewBox="0 0 22 22"><circle cx="11" cy="11" r="11" fill="#7a5bc8"/><path d="M6 11l3.5 3.5L16 8" stroke="#fff" stroke-width="2.2" fill="none"/></svg>Prüfung und Übernahme der Anmeldung verfügbarer Fördermöglichkeiten</li>
      <li><svg width="22" height="22" viewBox="0 0 22 22"><circle cx="11" cy="11" r="11" fill="#7a5bc8"/><path d="M6 11l3.5 3.5L16 8" stroke="#fff" stroke-width="2.2" fill="none"/></svg>Auswahl an smarten Wallbox Lösungen, passend für Ihr Fahrzeug und Ihre Bedürfnisse</li>
      <li><svg width="22" height="22" viewBox="0 0 22 22"><circle cx="11" cy="11" r="11" fill="#7a5bc8"/><path d="M6 11l3.5 3.5L16 8" stroke="#fff" stroke-width="2.2" fill="none"/></svg>Installation inkl. aller notwendigen Materialien und Tätigkeiten (Durchbrüche, Erdarbeiten, etc.)</li>
      <li><svg width="22" height="22" viewBox="0 0 22 22"><circle cx="11" cy="11" r="11" fill="#7a5bc8"/><path d="M6 11l3.5 3.5L16 8" stroke="#fff" stroke-width="2.2" fill="none"/></svg>Inbetriebnahme und Einweisung in die Ladetechnik</li>
      <li><svg width="22" height="22" viewBox="0 0 22 22"><circle cx="11" cy="11" r="11" fill="#7a5bc8"/><path d="M6 11l3.5 3.5L16 8" stroke="#fff" stroke-width="2.2" fill="none"/></svg>Jährlich technische Wartung nach DGUV3</li>
      <li><svg width="22" height="22" viewBox="0 0 22 22"><circle cx="11" cy="11" r="11" fill="#7a5bc8"/><path d="M6 11l3.5 3.5L16 8" stroke="#fff" stroke-width="2.2" fill="none"/></svg>Reparaturservice, unter Berücksichtigung der geltenden Garantie Ansprüche</li>
    </ul>
  </article>

  <article class="plan pink" style="left:428px">
    <div class="plan-head">
      <svg width="38" height="34" viewBox="0 0 38 34" fill="none" stroke="#fff" stroke-width="2"><circle cx="19" cy="10" r="6"/><circle cx="8" cy="13" r="4"/><circle cx="30" cy="13" r="4"/><path d="M9 32v-6a10 10 0 0 1 20 0v6M2 30v-4a6 6 0 0 1 6-6M36 30v-4a6 6 0 0 0-6-6"/></svg>
      <h3>als Geschäftskunde</h3>
    </div>
    <ul>
      <li><svg width="22" height="22" viewBox="0 0 22 22"><circle cx="11" cy="11" r="11" fill="#ec0c9f"/><path d="M6 11l3.5 3.5L16 8" stroke="#fff" stroke-width="2.2" fill="none"/></svg>Durchführung einer individuellen Bedarfsanalyse inkl.</li>
      <li><svg width="22" height="22" viewBox="0 0 22 22"><circle cx="11" cy="11" r="11" fill="#ec0c9f"/><path d="M6 11l3.5 3.5L16 8" stroke="#fff" stroke-width="2.2" fill="none"/></svg>Planung und Projektierung des Installationsaufwands inkl. Materialverbrauch</li>
      <li><svg width="22" height="22" viewBox="0 0 22 22"><circle cx="11" cy="11" r="11" fill="#ec0c9f"/><path d="M6 11l3.5 3.5L16 8" stroke="#fff" stroke-width="2.2" fill="none"/></svg>Leasing oder Kauf der Hardware</li>
      <li><svg width="22" height="22" viewBox="0 0 22 22"><circle cx="11" cy="11" r="11" fill="#ec0c9f"/><path d="M6 11l3.5 3.5L16 8" stroke="#fff" stroke-width="2.2" fill="none"/></svg>Normgerechte Installation der Ladeinfrastruktur inkl. Durchbruch-, Brandschutz- und Erdarbeiten</li>
      <li><svg width="22" height="22" viewBox="0 0 22 22"><circle cx="11" cy="11" r="11" fill="#ec0c9f"/><path d="M6 11l3.5 3.5L16 8" stroke="#fff" stroke-width="2.2" fill="none"/></svg>Bei Bestandsbauten Integration der Ladeinfrastruktur in die Gebäudesystemtechnik und ggf. Anpassung des Netzanschlusses</li>
      <li><svg width="22" height="22" viewBox="0 0 22 22"><circle cx="11" cy="11" r="11" fill="#ec0c9f"/><path d="M6 11l3.5 3.5L16 8" stroke="#fff" stroke-width="2.2" fill="none"/></svg>Inbetriebnahme der Anlage inkl. Prüf- und Messprotokollen</li>
      <li><svg width="22" height="22" viewBox="0 0 22 22"><circle cx="11" cy="11" r="11" fill="#ec0c9f"/><path d="M6 11l3.5 3.5L16 8" stroke="#fff" stroke-width="2.2" fill="none"/></svg>Wiederkehrende technische Prüfung der Anlage nach DGUV 3</li>
      <li><svg width="22" height="22" viewBox="0 0 22 22"><circle cx="11" cy="11" r="11" fill="#ec0c9f"/><path d="M6 11l3.5 3.5L16 8" stroke="#fff" stroke-width="2.2" fill="none"/></svg>Austausch und Reparatur Service</li>
      <li><svg width="22" height="22" viewBox="0 0 22 22"><circle cx="11" cy="11" r="11" fill="#ec0c9f"/><path d="M6 11l3.5 3.5L16 8" stroke="#fff" stroke-width="2.2" fill="none"/></svg>Unterstützung bei der mtl. Nutzungsabrechnung und Einbindung in Ihre vorhandene Abrechnungssysteme</li>
    </ul>
  </article>

  <article class="plan" style="left:794px">
    <div class="plan-head">
      <svg width="38" height="34" viewBox="0 0 38 34" fill="none" stroke="#fff" stroke-width="2"><circle cx="19" cy="10" r="6"/><circle cx="8" cy="13" r="4"/><circle cx="30" cy="13" r="4"/><path d="M9 32v-6a10 10 0 0 1 20 0v6M2 30v-4a6 6 0 0 1 6-6M36 30v-4a6 6 0 0 0-6-6"/></svg>
      <h3>als Kommune</h3>
    </div>
    <ul>
      <li><svg width="22" height="22" viewBox="0 0 22 22"><circle cx="11" cy="11" r="11" fill="#7a5bc8"/><path d="M6 11l3.5 3.5L16 8" stroke="#fff" stroke-width="2.2" fill="none"/></svg>Konzeptionierung möglicher Ladeinfrastrukturen innerhalb Ihrer Gemeinde</li>
      <li><svg width="22" height="22" viewBox="0 0 22 22"><circle cx="11" cy="11" r="11" fill="#7a5bc8"/><path d="M6 11l3.5 3.5L16 8" stroke="#fff" stroke-width="2.2" fill="none"/></svg>Planung und Projektsteuerung inkl. sämtlicher behördlicher Genehmigungsverfahren und Beantragung von Fördermitteln</li>
      <li><svg width="22" height="22" viewBox="0 0 22 22"><circle cx="11" cy="11" r="11" fill="#7a5bc8"/><path d="M6 11l3.5 3.5L16 8" stroke="#fff" stroke-width="2.2" fill="none"/></svg>Fachgerechte Installation und Inbetriebnahme</li>
      <li><svg width="22" height="22" viewBox="0 0 22 22"><circle cx="11" cy="11" r="11" fill="#7a5bc8"/><path d="M6 11l3.5 3.5L16 8" stroke="#fff" stroke-width="2.2" fill="none"/></svg>Regelmäßige Wartung gemäß Vorschrif</li>
      <li><svg width="22" height="22" viewBox="0 0 22 22"><circle cx="11" cy="11" r="11" fill="#7a5bc8"/><path d="M6 11l3.5 3.5L16 8" stroke="#fff" stroke-width="2.2" fill="none"/></svg>Reparatur und Kundenservice</li>
      <li><svg width="22" height="22" viewBox="0 0 22 22"><circle cx="11" cy="11" r="11" fill="#7a5bc8"/><path d="M6 11l3.5 3.5L16 8" stroke="#fff" stroke-width="2.2" fill="none"/></svg>Direkte Abrechnung mit dem Nutzer</li>
      <li><svg width="22" height="22" viewBox="0 0 22 22"><circle cx="11" cy="11" r="11" fill="#7a5bc8"/><path d="M6 11l3.5 3.5L16 8" stroke="#fff" stroke-width="2.2" fill="none"/></svg>Beteiligung der Gemeinde am Umsatz</li>
      <li><svg width="22" height="22" viewBox="0 0 22 22"><circle cx="11" cy="11" r="11" fill="#7a5bc8"/><path d="M6 11l3.5 3.5L16 8" stroke="#fff" stroke-width="2.2" fill="none"/></svg>Möglichkeit der Integration von Bonusprogrammen, mit denen der lokale Einzelhandel beworben wird</li>
    </ul>
  </article>
</section>

<section class="photo-band" role="img" aria-label="Close-up photo of a white charging plug in a socket ringed with glowing blue light"></section>

<section class="sustain">
  <div class="sustain-photo" role="img" aria-label="Photo of a charging station column with a plugged-in blue and yellow cable, city lights blurred behind"></div>
  <div class="sustain-copy">
    <p class="eyebrow">Save Nature</p>
    <h2 class="section-title">Sustainability is Our<br>Main Advantage</h2>
    <p>Lorem ipsum dolor sit amet, consectetur adipiscing elit, sed do eiusmod tempor incididunt ut labore.</p>
    <ul class="ticks">
      <li><svg width="12" height="10" viewBox="0 0 12 10"><path d="M1 5l3.5 3.5L11 1" stroke="#ec0c9f" stroke-width="2" fill="none"/></svg>Lorem ipsum dolor sit</li>
      <li><svg width="12" height="10" viewBox="0 0 12 10"><path d="M1 5l3.5 3.5L11 1" stroke="#ec0c9f" stroke-width="2" fill="none"/></svg>Ut enim ad minim veniam</li>
      <li><svg width="12" height="10" viewBox="0 0 12 10"><path d="M1 5l3.5 3.5L11 1" stroke="#ec0c9f" stroke-width="2" fill="none"/></svg>Duis aute irure dolor</li>
    </ul>
    <a class="btn btn-pink">About Us</a>
  </div>
</section>

<section class="reviews">
  <article class="review" style="left:-158px;height:496px">
    <div class="stars">★★★★★</div>
    <p>The station works fine and I've been charging daily. The cost isn't high and it saves money. Overall I am very happy and all the team was kind and helpful in every single step.</p>
  </article>
  <article class="review" style="left:157px;height:496px">
    <div class="stars">★★★★★</div>
    <p>I ordered the installation of a charging station, I was contacted immediately to discuss the details. The station was quickly and successfully installed. Excellent communication, excellent service and at a reasonable price.</p>
    <h4>Daniel Hart</h4><small>Business Coach</small>
  </article>
  <article class="review" style="left:472px;height:425px">
    <div class="stars">★★★★★</div>
    <p>These guys installed the station so quickly, and it works great! I even got a five-year warranty and a discount on future purchases! Absolutely love the service!</p>
    <h4>Mira Lenz</h4><small>PR Manager</small>
  </article>
  <article class="review" style="left:787px;height:425px">
    <div class="stars">★★★★★</div>
    <p>I purchased a new car battery at a great price! It holds a charge perfectly and lasts for a long time. Now I can go anywhere. I recommend it to everyone!</p>
    <h4>Oskar Brandt</h4><small>PR Manager</small>
  </article>
  <article class="review" style="left:1102px;height:496px">
    <div class="stars">★★★★★</div>
    <p>The charging station works fine without interruption and is powerful and quickly. Yes, as well as fuel, as we care for the environment, so that soon every motor will make use of fun.</p>
    <h4>Felix</h4><small>PR Manager</small>
  </article>
  <div class="slider-dots"><i class="on"></i><i></i><i></i><i></i><i></i></div>
</section>

<footer class="site-footer">
  <div class="footer-address">12 Lindenallee, Office 3<br>DE 10115 Berlin, Germany</div>
  <div class="footer-contact">info@mero-kant.de<br>+49 30 555 01 20</div>
  <div class="socials" aria-label="Social media"><span></span><span></span><span></span><span></span></div>
  <svg class="to-top" width="28" height="28" viewBox="0 0 28 28" fill="none" stroke="#fff" stroke-width="1.6"><path d="M14 20V8M9 13l5-5 5 5"/></svg>
</footer>

</body>
</html>
```